New Church Plant website for Brightvale Church

I would like a six page website designed that is clean and easy to navigate. The six pages will include (1) About Us (2) Home (3) Contact Us (4) Sermons (5) Donate (6) Ministries. There will be subcategories for each category as well. The color scheme can be found in the attached magazine of Brightvale. Much of the information found in the booklet will be used on the website. I would love to see a design that pops but still clean and easy to navigate. I have included a good deal of pictures for the creative. Please see the current website at brightvalechapel.example which is temporary as we are preparing for a launch. I would now like to create a long-term site.

Target Market(s)

People interested in Christian church

Number of Pages Required

5+ page

Font styles to use
Sans Serif

Colors
ffffff
f78f20

Requirements
Must have
• a site that pops but is clean and easy to navigate.

```html
<!DOCTYPE html>
<html lang="en">
<head>
<meta charset="utf-8">
<title>Brightvale Church</title>
<link href="https://fonts.googleapis.com/css2?family=Russo+One&family=Roboto:wght@400;500;700&display=swap" rel="stylesheet">
<style>
:root{
  --orange:#f78f20;
  --orange-soft:rgba(247,143,32,.88);
  --dark:#2b2b2b;
  --darker:#242424;
  --cream:#f9f5f0;
  --white:#ffffff;
  --grey-text:#8a8a8a;
  --card:#8a8a8a;
}
*{margin:0;padding:0;box-sizing:border-box}
html,body{width:1200px;height:3981px;overflow:hidden}
body{position:relative;font-family:"Roboto",sans-serif;background:var(--white);color:#333}
.abs{position:absolute}
.display{font-family:"Russo One",sans-serif}
section,footer{position:absolute;left:0;width:1200px;overflow:hidden}

/* hero */
.hero{top:0;height:720px;background:var(--dark)}
.hero-photo{left:769px;top:0;width:431px;height:720px;background:linear-gradient(160deg,#5a4a40,#2a211c 60%,#15110e)}
.hero-stage{left:485px;top:0;width:284px;height:720px;background:linear-gradient(180deg,#c9701c,#a75a16 70%,#6e3c10);opacity:.95}
.hero-stage::after{content:"";position:absolute;inset:0;background:var(--orange-soft)}
.ghost-word{font-family:"Russo One",sans-serif;color:rgba(255,255,255,.05);font-size:96px;transform:rotate(90deg);transform-origin:left top;white-space:nowrap}
.brand{font-family:"Russo One",sans-serif;color:var(--white);font-size:26px;display:flex;align-items:center;gap:8px}
.brand .dot{width:12px;height:12px;border-radius:50%;background:var(--orange)}
.menu-icon{left:1108px;top:53px;width:22px}
.menu-icon span{display:block;height:2px;background:var(--white);margin-bottom:4px}
.welcome-card{left:147px;top:307px;width:395px;height:213px;background:var(--white);box-shadow:0 6px 20px rgba(0,0,0,.25);text-align:center;padding-top:48px}
.welcome-card .l1{font-size:32px;color:var(--dark);letter-spacing:3px;line-height:1.1}
.welcome-card .l2{font-size:26px;color:var(--dark);letter-spacing:2px;line-height:1.1}
.welcome-card .l3{font-size:40px;color:var(--orange);letter-spacing:3px;line-height:1.3}
.orange-block{background:var(--orange)}
.rule{height:2px;background:var(--orange);width:101px}
.tagline{left:185px;top:567px;color:var(--white);font-size:14px}
.tagline b{color:var(--orange);font-weight:700}
.social-dot{width:10px;height:10px;border-radius:50%;background:var(--white)}

/* about */
.about{top:720px;height:680px;background:var(--cream)}
.section-title{font-family:"Russo One",sans-serif;font-size:36px;line-height:42px}
.t-dark{color:var(--dark)}.t-orange{color:var(--orange)}
.body-copy{font-size:14px;line-height:22.5px;color:var(--grey-text);letter-spacing:.4px}
.photo{background:linear-gradient(135deg,#3a2f2a,#5b4639 50%,#251d18)}
.quote-mark{font-family:"Russo One",sans-serif;color:var(--orange);font-size:48px;line-height:1}
.quote{font-size:13.5px;font-weight:700;color:var(--dark);text-align:center;line-height:22px;letter-spacing:.3px}
.cite{font-size:13px;color:var(--orange);letter-spacing:1px;font-weight:500}
.btn{background:var(--orange);color:var(--white);font-size:12px;display:flex;align-items:center;justify-content:center;box-shadow:0 4px 10px rgba(0,0,0,.2);letter-spacing:.5px}

/* sermons */
.sermons{top:1400px;height:669px;background:var(--dark)}
.schedule{left:415px;top:139px;width:530px;height:409px;background:rgba(235,235,235,.95);box-shadow:0 6px 20px rgba(0,0,0,.25)}
.schedule-mid{left:67px;top:0;width:287px;height:409px;background:#fdf3ea}
.col{text-align:center;width:140px;font-size:13.5px;color:var(--grey-text)}
.col .head{color:var(--dark);font-size:16px;margin-top:6px;margin-bottom:32px}
.col .row{height:39.5px;letter-spacing:.5px}

/* donate */
.donate{top:2069px;height:344px;background:var(--white)}

/* ministries */
.ministries{top:2413px;height:524px;background:var(--dark);text-align:center}
.min-card{background:var(--card);border:1.5px solid #b5731f}
.min-card.active{box-shadow:0 8px 20px rgba(0,0,0,.5)}
.dots{display:flex;gap:6px;align-items:center}
.dots span{width:9px;height:9px;border-radius:50%;background:#cfcfcf}
.dots span.on{width:20px;height:20px;background:var(--orange)}

/* contact */
.contact{top:2937px;height:653px;background:var(--cream)}
.field{left:66px;width:524px;border:1.5px solid #d6d6d6;background:var(--cream);font-size:12px;color:#a5a5a5;padding:13px 30px}
.map{left:650px;top:0;width:550px;height:653px;background:linear-gradient(160deg,#dfeadb,#cfe3c9 40%,#e6ebe4 80%,#d5e4d0)}

/* footer */
.site-footer{top:3590px;height:391px;background:var(--dark);color:var(--white)}
.footer-copy{font-size:14px;line-height:24.7px;color:var(--white)}
.footer-head{font-family:"Russo One",sans-serif;font-size:26px}
.links{font-size:14px;line-height:24.7px}
.info{font-size:13.5px;line-height:19px}
.bottom-bar{top:316px;left:0;width:1200px;height:75px;background:var(--darker);border-top:1px solid #3a3a3a;font-size:11.5px;color:#777}
.pay{width:18px;height:10px;border-radius:2px;background:var(--white)}
</style>
</head>
<body>

<section class="hero">
  <div class="abs hero-photo" role="img" aria-label="Pastor speaking on a stage before the congregation"></div>
  <div class="abs hero-stage" role="img" aria-label="Stage with music stand, washed in orange"></div>
  <div class="abs ghost-word" style="left:480px;top:90px">PREACHING</div>
  <div class="abs brand" style="left:69px;top:56px"><span class="dot"></span>Brightvale Church</div>
  <div class="abs menu-icon"><span></span><span></span><span></span></div>
  <div class="abs orange-block" style="left:0;top:499px;width:170px;height:116px"></div>
  <div class="abs welcome-card display">
    <div class="l1">Welcome</div>
    <div class="l2">To</div>
    <div class="l3">BRIGHTVALE</div>
  </div>
  <div class="abs rule" style="left:185px;top:549px"></div>
  <div class="abs tagline">A Multi-ETHNIC Church Planting <b>CHURCH</b></div>
  <div class="abs social-dot" style="left:1105px;top:625px"></div>
  <div class="abs social-dot" style="left:1105px;top:651px"></div>
  <div class="abs social-dot" style="left:1105px;top:676px"></div>
</section>

<section class="about">
  <div class="abs orange-block" style="left:482px;top:0;width:287px;height:88px"></div>
  <div class="abs photo" style="left:550px;top:47px;width:447px;height:561px;box-shadow:0 8px 24px rgba(0,0,0,.3)" role="img" aria-label="The pastor and his wife smiling together"></div>
  <div class="abs orange-block" style="left:877px;top:497px;width:323px;height:183px;opacity:.9"></div>
  <div class="abs section-title" style="left:96px;top:112px"><div class="t-dark">About</div><div class="t-orange">Brightvale</div></div>
  <div class="abs rule" style="left:96px;top:213px;width:60px"></div>
  <p class="abs body-copy" style="left:96px;top:231px;width:290px">Our mission is to be a gospel-centered, multi-ethnic, church planting church built on the pillars of Missions, Faith, Work and Economics.</p>
  <div class="abs quote-mark" style="left:281px;top:371px">&ldquo;</div>
  <p class="abs quote" style="left:98px;top:421px;width:410px">I value multi-ethnic ministry because I am a product of what can happen through multi-ethnic relationships.</p>
  <div class="abs cite" style="left:337px;top:478px">PASTOR DALE MORROW</div>
  <div class="abs btn" style="left:96px;top:518px;width:151px;height:42px">Learn More</div>
</section>

<section class="sermons">
  <div class="abs orange-block" style="left:482px;top:0;width:287px;height:669px"></div>
  <div class="abs photo" style="left:769px;top:0;width:431px;height:669px;background:linear-gradient(135deg,#5a3a26,#3a271c 55%,#1f1712)" role="img" aria-label="Smiling woman from the church leadership"></div>
  <div class="abs ghost-word" style="left:410px;top:148px;color:rgba(255,255,255,.1);font-size:84px">Sermons</div>
  <div class="abs section-title t-orange" style="left:96px;top:236px">Sermons</div>
  <p class="abs body-copy" style="left:96px;top:314px;width:290px;color:#dcdcdc">Our mission is to be a gospel-centered, multi-ethnic, church planting church built on the pillars of Missions, Faith, Work and Economics.</p>
  <div class="abs orange-block" style="left:0;top:468px;width:170px;height:116px"></div>
  <div class="abs schedule">
    <div class="abs schedule-mid"></div>
    <div class="abs col" style="left:51px;top:53px">
      <svg width="26" height="26" viewBox="0 0 24 24" fill="none" stroke="#f78f20" stroke-width="1.6"><rect x="3" y="5" width="18" height="16" rx="2"/><path d="M3 10h18M8 3v4M16 3v4M7 14h2M11 14h2M15 14h2M7 17h2M11 17h2"/></svg>
      <div class="head">Date</div>
      <div class="row">dd-mm-yy</div><div class="row">dd-mm-yy</div><div class="row">dd-mm-yy</div><div class="row">dd-mm-yy</div><div class="row">dd-mm-yy</div>
    </div>
    <div class="abs col" style="left:196px;top:53px">
      <svg width="26" height="26" viewBox="0 0 24 24" fill="none" stroke="#f78f20" stroke-width="1.6"><circle cx="12" cy="12" r="9"/><path d="M12 7v5l3 3"/></svg>
      <div class="head">Time</div>
      <div class="row">hh:mm</div><div class="row">hh:mm</div><div class="row">hh:mm</div><div class="row">hh:mm</div><div class="row">hh:mm</div>
    </div>
    <div class="abs col" style="left:339px;top:53px">
      <svg width="26" height="26" viewBox="0 0 24 24" fill="#f78f20"><path d="M12 2a7 7 0 0 0-7 7c0 5 7 13 7 13s7-8 7-13a7 7 0 0 0-7-7zm0 9.5A2.5 2.5 0 1 1 12 6.5a2.5 2.5 0 0 1 0 5z"/></svg>
      <div class="head">Location</div>
      <div class="row">Address</div><div class="row">Address</div><div class="row">Address</div><div class="row">Address</div><div class="row">Address</div>
    </div>
  </div>
</section>

<section class="donate">
  <div class="abs section-title" style="left:96px;top:54px"><div class="t-orange">Want to Donate For</div><div class="t-dark">Brightvale</div></div>
  <div class="abs rule" style="left:96px;top:158px;width:60px"></div>
  <p class="abs body-copy" style="left:96px;top:175px;width:590px">Lorem Ipsum is simply dummy text of the printing and typesetting industry. Lorem Ipsum has been the industry's standard dummy text.</p>
  <div class="abs btn" style="left:96px;top:242px;width:321px;height:42px">Click here for more Information</div>
  <svg class="abs" style="left:1034px;top:34px" width="166" height="275" viewBox="0 0 166 275">
    <polygon points="166,0 166,20 28,137 166,255 166,275 0,137" fill="#2b2b2b"/>
    <polygon points="166,28 46,137 166,247" fill="#f78f20"/>
  </svg>
</section>

<section class="ministries">
  <div class="abs display t-orange" style="left:0;width:1200px;top:30px;font-size:36px">Ministeries</div>
  <p class="abs" style="left:290px;width:620px;top:96px;font-size:14px;line-height:21px;color:#e8e8e8;letter-spacing:.3px">Lorem Ipsum is simply dummy text of the printing and typesetting industry. Lorem Ipsum has been the industry's standard dummy text ever since the 1500s.</p>
  <div class="abs min-card" style="left:71px;top:193px;width:187px;height:184px" role="img" aria-label="Ministry photo"></div>
  <div class="abs min-card" style="left:279px;top:193px;width:189px;height:184px" role="img" aria-label="Ministry photo"></div>
  <div class="abs min-card active" style="left:489px;top:176px;width:223px;height:218px" role="img" aria-label="Featured ministry photo"></div>
  <div class="abs min-card" style="left:735px;top:193px;width:187px;height:184px" role="img" aria-label="Ministry photo"></div>
  <div class="abs min-card" style="left:943px;top:193px;width:189px;height:184px" role="img" aria-label="Ministry photo"></div>
  <div class="abs dots" style="left:542px;top:464px"><span></span><span></span><span></span><span class="on"></span><span></span><span></span><span></span></div>
</section>

<section class="contact">
  <div class="abs display t-orange" style="left:0;width:675px;text-align:center;top:56px;font-size:36px">Contact</div>
  <div class="abs field" style="top:145px;height:38px;padding-top:11px">Name</div>
  <div class="abs field" style="top:203px;height:39px;padding-top:11px">Number</div>
  <div class="abs field" style="top:262px;height:39px;padding-top:11px">Email</div>
  <div class="abs field" style="top:321px;height:216px;padding-top:22px">Message</div>
  <div class="abs btn" style="left:462px;top:559px;width:126px;height:41px">Send</div>
  <div class="abs map" role="img" aria-label="Map showing the church location and nearby towns"></div>
</section>

<footer class="site-footer">
  <div class="abs brand" style="left:69px;top:70px;font-size:24px"><span class="dot"></span>Brightvale Church</div>
  <p class="abs footer-copy" style="left:68px;top:128px;width:250px">A Lakeshore-based, multi-ethnic, gospel-centered, church planting church built on the pillars of missions, faith, work and economics. Launching April 12, 2020.</p>
  <div class="abs footer-head" style="left:522px;top:70px">Quick Links</div>
  <div class="abs links" style="left:537px;top:126px">Home<br>About<br>Sermons<br>Donation<br>Ministeries<br>Contact</div>
  <div class="abs footer-head" style="left:889px;top:70px">Information</div>
  <svg class="abs" style="left:888px;top:127px" width="14" height="16" viewBox="0 0 24 24" fill="none" stroke="#fff" stroke-width="2"><path d="M12 2a7 7 0 0 0-7 7c0 5 7 13 7 13s7-8 7-13a7 7 0 0 0-7-7z"/><circle cx="12" cy="9" r="2.5"/></svg>
  <div class="abs info" style="left:917px;top:126px">Lorem Ipsum Is A Dummy<br>Text</div>
  <svg class="abs" style="left:888px;top:182px" width="15" height="15" viewBox="0 0 24 24" fill="#fff"><path d="M6.6 10.8a15 15 0 0 0 6.6 6.6l2.2-2.2c.3-.3.7-.4 1-.2 1.1.4 2.3.6 3.6.6.6 0 1 .4 1 1V20c0 .6-.4 1-1 1A17 17 0 0 1 3 4c0-.6.4-1 1-1h3.5c.6 0 1 .4 1 1 0 1.3.2 2.5.6 3.6.1.3 0 .7-.2 1z"/></svg>
  <div class="abs info" style="left:917px;top:180px">555-010-0188</div>
  <div class="abs display t-orange" style="left:919px;top:209px;font-size:16px">Donate</div>
  <div class="abs" style="left:919px;top:234px;display:flex;gap:3px"><span class="pay"></span><span class="pay"></span><span class="pay"></span><span class="pay"></span></div>
  <div class="abs bottom-bar">
    <div class="abs" style="left:0;width:1200px;top:28px;text-align:center">&copy; Copyright &copy;2019 Brightvale Church. Email Us For More Information.</div>
    <span class="abs social-dot" style="left:1045px;top:31px;background:#888"></span>
    <span class="abs social-dot" style="left:1079px;top:31px;background:#888"></span>
    <span class="abs social-dot" style="left:1114px;top:31px;background:#888"></span>
  </div>
</footer>

</body>
</html>
```